Elegant Business Card for Technology Company

Client is a supplier of innovative industrial communications and automation equipment since 2002. This contest is to gather fresh ideas for a redesign of the existing business card. Client is looking for design that best communicates tagline "Industrial Networking and Computing Specialist".

Design submissions should look modern, clean, elegant and professional. It should not be cluttered. Use white as the primary colour. Orange and black as secondary colour. Refer to jpeg File 1 on the current design.

Fonts used by Client used include Arial Regular, Arial Black, Roboto Regular, Roboto Black and Lato.

The winning design will be sent for offset printing using super white 250gsm artcard paper (open for suggestions).

Target Market(s)

System Engineers, Project Managers, Purchasing Managers from companies providing engineering services for Smart Cities.

Industry/Entity Type

Information Technology

Contact Information for Business Card

Refer to PDF File 3 for Business Card Details. Priority of short contact information would be as follows Name > Job Title > Email > Mobile > Web > Tel > Fax > Business Address >UEN (UEN represents company registration number)

Font styles to use
Sans Serif

Colors
ffffff
f37122
000000
5c5c5c

Requirements
Must have
• Refer to AI File 2 (Company Logo) & PDF File 3 (Information on Namecard)
Should not have
• No QR codes
• No Social Media Icons
• Do not create full Black or Orange colour background

```html
<!DOCTYPE html>
<html lang="en">
<head>
<meta charset="utf-8">
<title>KVR Business Card</title>
<link rel="stylesheet" href="https://fonts.googleapis.com/css2?family=Lato:wght@400;700;900&display=swap">
<style>
  :root {
    --white: #ffffff;
    --orange: #f37122;
    --black: #000000;
    --grey: #5c5c5c;
    --backdrop: #2b2b2b;
    --ink: #1c1c1c;
  }
  * { box-sizing: border-box; margin: 0; padding: 0; }
  html, body {
    width: 1200px; height: 1166px; overflow: hidden;
    background: var(--backdrop);
    font-family: "Lato", Arial, sans-serif;
    color: var(--ink);
  }
  .card {
    position: absolute; left: 150px;
    width: 900px; height: 514px;
    background: var(--white);
    overflow: hidden;
  }
  .card--front { top: 49px; }
  .card--back { top: 603px; }

  .brand {
    position: absolute; display: flex; align-items: center; gap: 18px;
  }
  .brand__dot {
    width: 78px; height: 78px; border-radius: 50%; background: var(--orange);
  }
  .brand__name {
    font-weight: 900; font-size: 96px; line-height: 1; color: var(--ink); letter-spacing: 2px;
  }
  .card--front .brand { left: 50%; top: 70px; transform: translateX(-50%); }

  .services {
    position: absolute; left: 0; right: 0; top: 272px;
    text-align: center; font-size: 21px; line-height: 1.45; color: var(--ink);
  }
  .services .sep { color: var(--orange); padding: 0 6px; }

  .tagline-band {
    position: absolute; left: 0; right: 0; top: 402px; height: 56px;
    background: var(--ink);
    display: flex; align-items: center; justify-content: center;
  }
  .tagline {
    color: var(--white); font-size: 24px; letter-spacing: 1.5px; text-transform: uppercase;
  }

  .card--back .brand { right: 110px; top: 40px; }
  .company-id {
    position: absolute; right: 80px; top: 160px; width: 380px;
    text-align: right; font-size: 23px; padding-bottom: 8px;
    border-bottom: 1.5px solid var(--ink);
  }
  .address {
    position: absolute; right: 80px; top: 232px;
    text-align: right; font-size: 22px; line-height: 1.3; font-style: normal;
  }
  .person { position: absolute; left: 80px; top: 205px; width: 340px; }
  .person__name { font-size: 36px; line-height: 1.1; }
  .person__title { font-size: 25px; color: var(--orange); padding-bottom: 10px; border-bottom: 1.5px solid var(--ink); }
  .contacts { list-style: none; margin-top: 10px; }
  .contacts li { display: flex; align-items: center; gap: 16px; font-size: 22px; line-height: 1.4; }
  .contacts svg { width: 20px; height: 20px; flex: none; fill: var(--orange); }
</style>
</head>
<body>

<section class="card card--front">
  <div class="brand">
    <span class="brand__dot"></span>
    <span class="brand__name">KVR</span>
  </div>
  <p class="services">
    Industrial Ethernet / Wireless / Cellular<span class="sep">•</span>Industrial and Embedded Computing<br>
    Serial / Fieldbus Connectivity<span class="sep">•</span>IP Video Surveillance<span class="sep">•</span>Remote Automation
  </p>
  <div class="tagline-band">
    <span class="tagline">Industrial Networking and Computing Specialist</span>
  </div>
</section>

<section class="card card--back">
  <div class="brand">
    <span class="brand__dot"></span>
    <span class="brand__name">KVR</span>
  </div>
  <p class="company-id">UEN No 201804417K</p>
  <address class="address">
    KVR Asia Pacific Pte Ltd<br>
    22 Harbour Lane<br>
    Northpoint Hub #05-12 (Lobby B)<br>
    Singapore 418920
  </address>

  <div class="person">
    <p class="person__name">Daniel Reyes</p>
    <p class="person__title">Sales manager</p>
    <ul class="contacts">
      <li><svg viewBox="0 0 20 20" aria-hidden="true"><path d="M4 2l4 1 1 4-2 2a11 11 0 0 0 4 4l2-2 4 1 1 4-2 2C9 18 2 11 2 4z"/></svg>+65 6100 2040</li>
      <li><svg viewBox="0 0 20 20" aria-hidden="true"><path d="M6 1h8a1 1 0 0 1 1 1v16a1 1 0 0 1-1 1H6a1 1 0 0 1-1-1V2a1 1 0 0 1 1-1zm1 2v11h6V3zm3 12.5a1 1 0 1 0 0 2 1 1 0 0 0 0-2z"/></svg>+65 9100 3050</li>
      <li><svg viewBox="0 0 20 20" aria-hidden="true"><path d="M5 1h8l2 2v4H5zM2 8h16a1 1 0 0 1 1 1v7h-3v3H4v-3H1V9a1 1 0 0 1 1-1zm4 6v3h8v-3z"/></svg>+65 6100 2041</li>
      <li><svg viewBox="0 0 20 20" aria-hidden="true"><path d="M1 4h18v12H1zm2 2v.5l7 5 7-5V6l-7 5z"/></svg>sales@kvr.com.sg</li>
      <li><svg viewBox="0 0 20 20" aria-hidden="true"><path d="M10 1a9 9 0 1 0 0 18 9 9 0 0 0 0-18zm0 2c1 1 2 3 2.3 6H7.7C8 6 9 4 10 3zM3.1 9A7 7 0 0 1 7 3.6 13 13 0 0 0 5.7 9zm0 2h2.6A13 13 0 0 0 7 16.4 7 7 0 0 1 3.1 11zm4.6 0h4.6c-.3 3-1.3 5-2.3 6-1-1-2-3-2.3-6zm6.6 0h2.6a7 7 0 0 1-3.9 5.4 13 13 0 0 0 1.3-5.4zm0-2A13 13 0 0 0 13 3.6 7 7 0 0 1 16.9 9z"/></svg>www.kvr.com.sg</li>
    </ul>
  </div>
</section>

</body>
</html>
```